BrightQuill PowerPoint Design

We need a very cool power-point template done for BrightQuill. We need it to drive the message of technology, speed and innovation. This is for a racing proposal to for our indy car team. I will attach our logo.

Target Market(s)

This presentation is for our INDY RACE CAR TEAM OVERVIEW... The Theme is: Speed, Technology and Innovation

Industry/Entity Type

Racing

Colors

Designer to choose colors to be used in the design.

Requirements
Must have
• Intro Slide with Logo - Must look very cool
Template Slide for Content
Ending Slide with something like "Thanks BrightQuill!"
Nice to have
• Please see the example ppt deck from Lomerix a previous company to see the slide template... Also see a old template for BrightQuill

```html
<!DOCTYPE html>
<html lang="en">
<head>
<meta charset="utf-8">
<title>BrightQuill – Title Slide</title>
<link href="https://fonts.googleapis.com/css2?family=Questrial&family=Carlito&display=swap" rel="stylesheet">
<style>
  :root {
    --bg-navy: #03164b;
    --brand-blue: #2f8cc6;
    --title-blue: #2b87c5;
    --body-blue: #3a8dd3;
    --divider: rgba(70, 120, 190, 0.45);
  }
  html, body {
    margin: 0;
    padding: 0;
    overflow: hidden;
    background: var(--bg-navy);
  }
  .slide {
    position: relative;
    width: 1200px;
    height: 900px;
    overflow: hidden;
    background: var(--bg-navy);
  }
  .spectrum-glow {
    position: absolute;
    left: 0;
    top: 0;
    width: 1200px;
    height: 420px;
    background: linear-gradient(90deg,
      #5a1a4a 0%, #7a2a3a 8%, #8a5a20 16%, #9a8a2a 26%,
      #7aa030 36%, #2e9a5a 46%, #1f8a8a 56%, #1f7ab0 66%,
      #2a5aa8 76%, #4a3a9a 86%, #3a2a78 100%);
    opacity: 0.75;
    filter: blur(14px);
    -webkit-mask-image: radial-gradient(ellipse 60% 70% at 50% 30%, #000 35%, transparent 100%);
    mask-image: radial-gradient(ellipse 60% 70% at 50% 30%, #000 35%, transparent 100%);
  }
  .brand-name {
    position: absolute;
    left: 118px;
    top: 532px;
    margin: 0;
    font-family: "Questrial", sans-serif;
    font-size: 58px;
    font-weight: 400;
    color: var(--brand-blue);
    letter-spacing: 0.5px;
  }
  .divider {
    position: absolute;
    left: 554px;
    top: 472px;
    width: 2px;
    height: 176px;
    background: linear-gradient(180deg, transparent, var(--divider) 25%, var(--divider) 75%, transparent);
  }
  .project-title {
    position: absolute;
    left: 607px;
    top: 476px;
    margin: 0;
    font-family: "Questrial", sans-serif;
    font-size: 50px;
    font-weight: 400;
    color: var(--title-blue);
  }
  .project-summary {
    position: absolute;
    left: 608px;
    top: 548px;
    width: 480px;
    margin: 0;
    font-family: "Carlito", sans-serif;
    font-size: 19.5px;
    line-height: 30px;
    color: var(--body-blue);
  }
</style>
</head>
<body>
  <main class="slide">
    <div class="spectrum-glow" role="img" aria-label="Blurred colourful audio equalizer bars glowing across the top of the slide"></div>

    <h2 class="brand-name">BrightQuill</h2>

    <div class="divider"></div>

    <h1 class="project-title">Project Title Here</h1>
    <p class="project-summary">Lorem ipsum dolor sit lorem ipsum dolor sit Lorem ipsum dolor sit lorem ipsum dolor sit Lorem ipsum dolor sit lorem ipsum dolor sit</p>
  </main>
</body>
</html>
```